依頼詳細
新春キャンペーンに向けてのチラシの作成をお願いします。
暁光時報の折り込みチラシ用を想定しています。

<入会特典>
パーソナルジム通常入会金22,000円→0円
事務手数料→0円
プロテイン3kg分プレゼント

基本メニューは下記になります。

スタンダードコースご利用料金
262,000円(税込)16回×50分
(上下ウェア・タオル・ドリンク・プロテイン)

以前他のパーソナルトレーニングジム会員の方 乗り換え特典で更にお得
224,000円(税込)16回×50分
(上下ウェア・タオル・ドリンク・プロテイン)

スタンダードコース終了後 更にお得な継続コースをご用意。

継続プラン
116,000円(税込)8回×50分
224,000円(税込)16回×50分
324,000円(税込)24回×50分
(上下ウェア・タオル・ドリンク・プロテイン)
記載項目
K VORTA 浦和店
〒338–0472
埼玉県さいたま市浦和区若葉台7-15八幡ビル4階
☎︎048-592-7716
サイズ
B4
ページ数
両面
希望イメージ
シンプル 複雑
単色 カラフル
暗い 明るい
日常 高級
遊び心 厳粛
未来的 伝統的
女性的 男性的
希望する色
赤系、黄・オレンジ系、無彩色系、金色
納品ファイル
• イラストレーター形式 (.ai)
補足説明
①添付のビフォーアフター写真、及び下記体組計データを掲載して
『2ヶ月で人はここまで変わる』というメッセージを打ち出したいです。

<女性>
お腹周り91cm→68cm
腕周り33cm→28cm
太腿周り59cm→52cm
体重63.05kg→51.95kg
体脂肪率40%→28%

<男性>
お腹周り98cm→77cm
腕周り36cm→35cm
太腿周り59cm→55cm
体重81.50kg→64.90kg
体脂肪率30%→13%

②チラシ裏面に、在籍トレーナーや店舗設備の写真を掲載して
店舗の雰囲気が伝わるように表現をして頂きたいです。
スペースの関係上難しい場合は、店舗設備の写真は不要でも問題ありません。

③添付ロゴを黒背景のオレンジ文字に変換して掲載をお願い致します。
添付のスタッフ写真には『ケイヴォルタ浦和店マネージャー倉持』と記載頂けますと幸いです。

<PRポイント>
■年間200名のお客様を担当
■8ヶ月で最大40kgのダイエット指導実績
■目標達成率98.7%を誇る指導力
■自ら3ヶ月で15kgのダイエットに成功
■フィットスターアジア2019さいたま大会グランプリ受賞

デザインや色合い、写真の加工や情報の表現について、こちらの理想通りに仕上げて頂きました。
また、細部にまで細かい配慮をして頂き非常に助かりました。ありがとうございます!!

ご提案頂きましたランサーの方々、お忙しい中データ作成して頂きまして誠にありがとうございます。
大変恐縮ながら、今回は当選者の方のご提案でお願いする運びとなりました。またご機会がございましたら何卒よろしくお願い申し上げます。

```html
<!DOCTYPE html>
<html lang="ja">
<head>
<meta charset="utf-8">
<title>2ヶ月で人はここまで変わる</title>
<link href="https://fonts.googleapis.com/css2?family=Noto+Serif+JP:wght@500;700;900&display=swap" rel="stylesheet">
<style>
  :root {
    --ink: #000000;
    --paper: #f4f1ea;
    --gold: #c9a46a;
    --gold-deep: #a9834a;
    --rule: #6b5a3e;
    --photo-dark: #1a1a1a;
    --photo-mid: #4a4038;
  }
  * { margin: 0; padding: 0; box-sizing: border-box; }
  html, body { width: 849px; height: 1200px; overflow: hidden; background: var(--ink); }
  .flyer {
    position: relative; width: 849px; height: 1200px; overflow: hidden;
    background: var(--ink); color: var(--paper);
    font-family: "Noto Serif JP", serif;
  }
  .headline {
    position: absolute; top: 18px; left: 0; width: 100%;
    text-align: center; font-size: 58px; font-weight: 900; letter-spacing: 2px;
    color: var(--paper);
  }
  .photo {
    position: absolute;
    background: linear-gradient(180deg, var(--photo-dark) 0%, var(--photo-mid) 50%, var(--photo-dark) 100%);
  }
  .photo--woman-before { left: 22px; top: 140px; width: 190px; height: 470px; }
  .photo--woman-after { left: 245px; top: 140px; width: 185px; height: 470px; }
  .photo--man-after { left: 440px; top: 650px; width: 195px; height: 460px; }
  .photo--man-before { left: 645px; top: 650px; width: 195px; height: 460px; }
  .arrow { position: absolute; }
  .arrow--women { left: 208px; top: 322px; }
  .arrow--men { left: 620px; top: 720px; }
  .section-head {
    position: absolute; display: flex; align-items: center; gap: 14px;
    font-size: 30px; font-weight: 700; letter-spacing: 6px; color: var(--paper);
  }
  .section-head--women { left: 478px; top: 148px; }
  .section-head--men { left: 22px; top: 640px; }
  .ornament { display: block; }
  .stats { position: absolute; list-style: none; }
  .stats--women { left: 470px; top: 262px; width: 360px; }
  .stats--men { left: 22px; top: 728px; width: 410px; }
  .stat {
    display: flex; align-items: baseline; gap: 10px;
    padding: 4px 0 6px 8px; border-bottom: 1px solid var(--rule);
    white-space: nowrap;
  }
  .stat__label { font-size: 22px; font-weight: 700; width: 96px; }
  .stat__before { font-size: 22px; font-weight: 500; }
  .stat__after { font-size: 44px; font-weight: 700; color: var(--gold); line-height: 1; }
  .stats--body { position: absolute; list-style: none; }
  .stats--body-women { left: 470px; top: 464px; width: 360px; }
  .stats--body-men { left: 22px; top: 966px; width: 410px; }
  .stats--body .stat { border-bottom: none; padding-bottom: 2px; }
  .footer-note {
    position: absolute; left: 0; top: 1140px; width: 100%;
    text-align: center; font-size: 26px; font-weight: 700; letter-spacing: 1px;
  }
</style>
</head>
<body>
<main class="flyer">
  <h1 class="headline">2ヶ月で人はここまで変わる</h1>

  <div class="photo photo--woman-before" role="img" aria-label="トレーニング前の女性の全身写真"></div>
  <div class="photo photo--woman-after" role="img" aria-label="2ヶ月後の女性の全身写真"></div>
  <svg class="arrow arrow--women" width="44" height="36" viewBox="0 0 44 36" aria-hidden="true">
    <path d="M2 18 H34 M22 5 L36 18 L22 31" fill="none" stroke="#f4f1ea" stroke-width="5"/>
  </svg>

  <h2 class="section-head section-head--women">
    <svg class="ornament" width="90" height="12" viewBox="0 0 90 12" aria-hidden="true">
      <line x1="0" y1="6" x2="80" y2="6" stroke="#f4f1ea" stroke-width="1.5"/>
      <path d="M80 6 L85 1 L90 6 L85 11 Z" fill="#f4f1ea"/>
    </svg>
    女性
    <svg class="ornament" width="90" height="12" viewBox="0 0 90 12" aria-hidden="true">
      <path d="M0 6 L5 1 L10 6 L5 11 Z" fill="#f4f1ea"/>
      <line x1="10" y1="6" x2="90" y2="6" stroke="#f4f1ea" stroke-width="1.5"/>
    </svg>
  </h2>

  <ul class="stats stats--women">
    <li class="stat"><span class="stat__label">腕周り</span><span class="stat__before">33cm→</span><span class="stat__after">28cm</span></li>
    <li class="stat"><span class="stat__label">お腹周り</span><span class="stat__before">91cm→</span><span class="stat__after">68cm</span></li>
    <li class="stat"><span class="stat__label">太腿周り</span><span class="stat__before">59cm→</span><span class="stat__after">52cm</span></li>
  </ul>
  <ul class="stats stats--body stats--body-women">
    <li class="stat"><span class="stat__label">体重</span><span class="stat__before">63.05kg→</span><span class="stat__after">51.95kg</span></li>
    <li class="stat"><span class="stat__label">体脂肪率</span><span class="stat__before">40%→</span><span class="stat__after">28%</span></li>
  </ul>

  <h2 class="section-head section-head--men">
    <svg class="ornament" width="90" height="12" viewBox="0 0 90 12" aria-hidden="true">
      <line x1="0" y1="6" x2="80" y2="6" stroke="#f4f1ea" stroke-width="1.5"/>
      <path d="M80 6 L85 1 L90 6 L85 11 Z" fill="#f4f1ea"/>
    </svg>
    男性
    <svg class="ornament" width="90" height="12" viewBox="0 0 90 12" aria-hidden="true">
      <path d="M0 6 L5 1 L10 6 L5 11 Z" fill="#f4f1ea"/>
      <line x1="10" y1="6" x2="90" y2="6" stroke="#f4f1ea" stroke-width="1.5"/>
    </svg>
  </h2>

  <ul class="stats stats--men">
    <li class="stat"><span class="stat__label">腕周り</span><span class="stat__before">36cm→</span><span class="stat__after">35cm</span></li>
    <li class="stat"><span class="stat__label">お腹周り</span><span class="stat__before">98cm→</span><span class="stat__after">77cm</span></li>
    <li class="stat"><span class="stat__label">太腿周り</span><span class="stat__before">59cm→</span><span class="stat__after">55cm</span></li>
  </ul>
  <ul class="stats stats--body stats--body-men">
    <li class="stat"><span class="stat__label">体重</span><span class="stat__before">81.50kg→</span><span class="stat__after">64.90kg</span></li>
    <li class="stat"><span class="stat__label">体脂肪率</span><span class="stat__before">30%→</span><span class="stat__after">13%</span></li>
  </ul>

  <div class="photo photo--man-after" role="img" aria-label="2ヶ月後の男性の全身写真"></div>
  <div class="photo photo--man-before" role="img" aria-label="トレーニング前の男性の全身写真"></div>
  <svg class="arrow arrow--men" width="44" height="36" viewBox="0 0 44 36" aria-hidden="true">
    <path d="M42 18 H10 M22 5 L8 18 L22 31" fill="none" stroke="#f4f1ea" stroke-width="5"/>
  </svg>

  <p class="footer-note">この効果をぜひ体感してください。詳しくは裏面にて</p>
</main>
</body>
</html>
```